Renamed Motel Needs Appealing Flyer

We need a flyer design for a motel that has been closed for 3 years and has just reopened under new management. It has been renamed 'Tallowind Motel' and is located in the Grampians in Vic. We would like our design to showcase the beauty and magnificence of the Grampians National Park (Gariwerd being the Aboriginal name for the Park). The motel is an older style building, so we don't want photos of the building to be the focus of the flyer until we have had time to renovate etc.
http://www.filedrovex.com/file/9tq2pm
I will add a high res image of the motel name/logo on Monday
http://www.filedrovex.com/file/9tq2pm to see an additional photo. I will add a high res image of motel name/logo on Monday
all ages, backpackers, budget consious travellers, seniors, groups
- Flyer must be DL size (front and back only) with logo at the top so that it is visible when displayed in a tiered display rack. I am not sure if the logo I have provided is adequate resolution wise. Can you let me know if it is not? The 'points' under the name are not part of the logo and should be removed.
Suggested wording for front of flyer - Surrounded by rugged mountain ranges and native plants and animals, Tallowind Motel is the perfect base to explore the natural beauty of the Grampians.
Back of flyer - features: affordable accommodation, 25 spacious ground floor rooms,
single/twin/triple/quadruple rooms; queen beds; ensuite bathrooms/some rooms with baths; toaster/ tea and coffee making facilities; iron/ironing board in rooms; digital TV; free WiFi; microwaves for guest use; free BBQ facilities; breakfast available; conference facility for up to 25 persons
Address - 14 Brackley Rd, Mossvale 3274
Phone: (03) 5471 2098
Email: tallowindmotel@quokmail.com
www.tallowindmotel.com.au
Updated after first set of submissions/comments - 10.55 PM AEST.
The following text only should be for the front of the brochure - Surrounded by rugged mountain ranges and native plants and animals, Tallowind Motel is the perfect base to explore the natural beauty of the Grampians.
Logically then, listings from the original brief such as 'Surrounded by mountains' would not be relevant for the back.
The dot points listed above in the first brief, should then be the focus for the information and detail on the back of the brochure.
Another update is;
- correct display is R/Trak
- I would like the flyer to have a flowing feel, print over top of scenery images, different fonts. Perhaps back of flyer could be printed over a washed image of Grampians

```html
<!DOCTYPE html>
<html lang="en">
<head>
<meta charset="utf-8">
<title>Tallowind Motel – DL Flyer</title>
<link rel="stylesheet" href="https://fonts.googleapis.com/css2?family=Arimo:wght@400;700&family=Noto+Sans:wght@400;700&family=Archivo+Narrow:wght@700&display=swap">
<style>
  :root {
    --green: #0b4a1e;
    --green-text: #1f4a20;
    --cream: #f1eeb4;
    --gold: #b8952a;
    --frame-dark: #231f20;
    --strip-grey: #6d6d6d;
    --white: #ffffff;
  }
  html, body {
    margin: 0;
    padding: 0;
    width: 1200px;
    height: 1178px;
    overflow: hidden;
    background: var(--white);
  }
  .sheet {
    position: absolute;
    left: 0;
    top: 0;
    width: 825px;
    height: 809px;
    transform: scale(1.4545, 1.4561);
    transform-origin: 0 0;
  }
  .panel {
    position: absolute;
    top: 15px;
    width: 390px;
    height: 780px;
    background: linear-gradient(180deg, var(--gold) 0%, #8e7a3a 30%, #3a342a 60%, var(--frame-dark) 75%, var(--frame-dark) 100%);
  }
  .panel--front { left: 15px; }
  .panel--back { left: 420px; }
  .panel__inner {
    position: absolute;
    left: 18px;
    top: 18px;
    width: 354px;
    height: 744px;
    background: var(--white);
    overflow: hidden;
  }
  .masthead {
    position: absolute;
    left: 0; top: 0;
    width: 100%;
    height: 170px;
    background: var(--green);
    text-align: center;
  }
  .brand-name {
    position: absolute;
    left: 0; right: 0;
    top: 58px;
    margin: 0;
    font-family: "Arimo", Arial, sans-serif;
    font-weight: 700;
    font-size: 34px;
    color: var(--cream);
    letter-spacing: 0.5px;
  }
  .panel--back .brand-name { top: 50px; }
  .masthead__tagline {
    position: absolute;
    left: 0; right: 0;
    top: 129px;
    margin: 0;
    font-family: "Arimo", Arial, sans-serif;
    font-weight: 700;
    font-size: 14px;
    color: var(--white);
  }
  .divider {
    position: absolute;
    left: 0;
    top: 170px;
    width: 100%;
    height: 7px;
  }
  .divider--grey { background: var(--strip-grey); }
  .divider--white { background: var(--white); }
  .band {
    position: absolute;
    left: 0;
    top: 177px;
    width: 100%;
    height: 11px;
    background: var(--green);
  }
  .scenery {
    position: absolute;
    left: 0;
    top: 188px;
    width: 100%;
    height: 340px;
    background:
      linear-gradient(180deg, rgba(255,255,255,0) 62%, rgba(255,255,255,0.6) 82%, var(--white) 100%),
      linear-gradient(180deg, #5d5b6c 0%, #7a6e72 14%, #9c7c4c 30%, #a3824a 44%, #6a6a3a 58%, #4f6a38 72%, #6f8460 100%);
  }
  .front-message {
    position: absolute;
    left: 10px;
    right: 10px;
    top: 518px;
    margin: 0;
    text-align: center;
    font-family: "Noto Sans", Verdana, sans-serif;
    font-size: 15px;
    line-height: 21px;
    color: var(--green-text);
  }
  .features {
    position: absolute;
    left: 0;
    right: 0;
    top: 205px;
    text-align: center;
    font-family: "Noto Sans", Verdana, sans-serif;
    font-size: 11.6px;
    line-height: 14px;
    color: var(--green-text);
  }
  .features h2 {
    margin: 0;
    font-family: "Archivo Narrow", "Arial Narrow", sans-serif;
    font-weight: 700;
    font-size: 14px;
    line-height: 15px;
    letter-spacing: 0.4px;
    color: var(--green);
  }
  .features ul {
    list-style: none;
    margin: 0 0 8px;
    padding: 0;
  }
  .room-photo {
    position: absolute;
    left: 32px;
    top: 462px;
    width: 280px;
    height: 146px;
    border: 5px solid var(--green);
    border-radius: 18px;
    background: linear-gradient(180deg, #e6e8e4 0%, #d6d8d2 45%, #6f86a8 62%, #4e6d92 80%, #3e4a52 100%);
  }
  .contact {
    position: absolute;
    left: 0;
    top: 639px;
    width: 100%;
    height: 105px;
    background: var(--green);
    text-align: center;
    font-family: "Arimo", Arial, sans-serif;
    font-size: 14px;
    line-height: 16.5px;
    color: var(--white);
    font-style: normal;
  }
  .contact p { margin: 0; }
  .contact p:first-child { margin-top: 14px; }
</style>
</head>
<body>
<main class="sheet">

  <section class="panel panel--front">
    <div class="panel__inner">
      <header class="masthead">
        <h1 class="brand-name">Tallowind Motel</h1>
      </header>
      <div class="divider divider--grey"></div>
      <div class="band"></div>
      <div class="scenery" role="img" aria-label="Rugged sandstone mountain peak of the Grampians above green bushland at dusk"></div>
      <p class="front-message">Surrounded by rugged mountain ranges<br>and native plants and animals,<br>Tallowind Motel is the perfect<br>base to explore the natural beauty of<br>the Grampians.</p>
      <address class="contact">
        <p>14 Brackley Rd, Mossvale 3274</p>
        <p>Phone: (03) 5471 2098</p>
        <p>Email: tallowindmotel@quokmail.com</p>
        <p>www.tallowindmotel.com.au</p>
      </address>
    </div>
  </section>

  <section class="panel panel--back">
    <div class="panel__inner">
      <header class="masthead">
        <h1 class="brand-name">Tallowind Motel</h1>
        <p class="masthead__tagline">Grampians National Park, Western Victoria</p>
      </header>
      <div class="divider divider--white"></div>
      <div class="band"></div>
      <div class="features">
        <h2>KEY FEATURES</h2>
        <ul>
          <li>Motel is an easy 5 minute walk from the centre of</li>
          <li>Halls Gap,</li>
          <li>100 metres from R/Trak bus stop,</li>
          <li>Affordable accommodation,</li>
          <li>25 spacious ground floor rooms</li>
        </ul>
        <h2>FEATURES</h2>
        <ul>
          <li>Single/twin/triple/quadruple rooms,</li>
          <li>Queen beds,</li>
          <li>Ensuite bathrooms/some rooms with baths,</li>
          <li>Toaster/ tea and coffee making facilities,</li>
          <li>Iron/ironing board in rooms,</li>
          <li>Digital TV, Free WiFi,</li>
          <li>Microwaves for guest use,</li>
          <li>Free BBQ facilities, Breakfast available,</li>
          <li>Conference facility for up to 25 persons</li>
        </ul>
      </div>
      <div class="room-photo" role="img" aria-label="Motel room with two single beds in patterned blue covers, bedside lamp and kitchenette"></div>
      <address class="contact">
        <p>14 Brackley Rd, Mossvale 3274</p>
        <p>Phone: (03) 5471 2098</p>
        <p>Email: tallowindmotel@quokmail.com</p>
        <p>www.tallowindmotel.com.au</p>
      </address>
    </div>
  </section>

</main>
</body>
</html>
```